Logo design and Businesscard and letterhead for Technology Company

We need logo design for a new company based in Atlanta called "Plovenix". We provide information about technology Product and service provider companies, information about their Products and services. Our initial focus is to List various companies and their products, various consulting companies and their services. We want to convey the message that this will be one stop shop to find out all the information to make smart technology decisions

I am looking for Logo, Business Card and Letterhead.

Target Market(s)

Companies that have IT department, IT users such as Developers, Managers, C level, Technology Product companies , Consulting companies and service providers.

Industry/Entity Type

It Company

Requirements
Must have
• Looking for some Unique design idea.
Nice to have
• I want something that connects information across technologies between technology buyers and sellers.
Should not have
• No puzzle design.

```html
<!DOCTYPE html>
<html lang="en">
<head>
<meta charset="utf-8">
<title>Plovenix – Stationery</title>
<link href="https://fonts.googleapis.com/css2?family=Libre+Baskerville:wght@700&family=Oswald:wght@300;500&display=swap" rel="stylesheet">
<style>
  :root{
    --brand-red:#c1272d;
    --slate:#4b5a66;
    --slate-text:#a9b4bc;
    --leaf:#6a9a2d;
    --paper:#ffffff;
    --line:#e6e6e6;
    --mark-tint:#e3eadb;
  }
  *{margin:0;padding:0;box-sizing:border-box}
  html,body{width:963px;height:1200px;overflow:hidden;background:var(--paper)}
  .canvas{position:relative;width:963px;height:1200px;background:var(--paper)}
  .crop{position:absolute;background:#555}
  .sheet-edge{position:absolute;left:48px;top:51px;width:868px;height:1098px;border:1px solid var(--line)}
  .backdrop-area{position:absolute;left:48px;top:218px;width:640px;height:820px;
    background:radial-gradient(ellipse at 45% 55%, var(--mark-tint) 0%, rgba(227,234,219,.5) 55%, rgba(255,255,255,0) 75%)}
  .header{position:absolute;left:48px;top:51px;width:868px;height:138px;background:var(--brand-red)}
  .header .brand{position:absolute;left:32px;top:52px}
  .header .rule{position:absolute;left:290px;top:94px;width:578px;height:1px;background:rgba(255,255,255,.8)}
  .contact-bar{position:absolute;left:48px;top:189px;width:868px;height:29px;background:var(--slate);
    display:flex;align-items:center;padding-left:95px;gap:8px;
    font-family:"Oswald",sans-serif;font-weight:300;font-size:13px;letter-spacing:.6px;color:var(--slate-text)}
  .contact-bar b{font-weight:500;color:#fff}
  .contact-bar .sep{color:#8b979f}
  .brand{display:flex;align-items:center;gap:10px;font-family:"Libre Baskerville",serif;font-weight:700;color:#fff}
  .brand .dot{border-radius:50%;background:var(--leaf);flex:none}
  .header .brand{font-size:27px}
  .header .brand .dot{width:40px;height:40px}
  .hero{position:absolute;left:413px;top:405px;width:400px;text-align:center}
  .hero .dot{width:112px;height:112px;border-radius:50%;background:var(--leaf);margin:0 auto 44px}
  .hero .name{font-family:"Libre Baskerville",serif;font-weight:700;font-size:64px;line-height:1;color:var(--slate);letter-spacing:2px}
  .card{position:absolute;top:784px;width:268px;height:163px;border-radius:6px;overflow:hidden}
  .card-front{left:227px;background:var(--brand-red)}
  .card-front .brand{position:absolute;left:14px;top:70px;font-size:15px;gap:7px}
  .card-front .brand .dot{width:22px;height:22px}
  .card-front .rule{position:absolute;left:135px;top:84px;width:133px;height:1px;background:rgba(255,255,255,.8)}
  .card-back{left:585px;background:var(--slate)}
  .card-back .strip{position:absolute;right:0;top:0;width:25px;height:100%;background:var(--brand-red);
    display:flex;align-items:center;justify-content:center}
  .card-back .strip span{writing-mode:vertical-rl;font-family:"Oswald",sans-serif;font-weight:300;font-size:8px;letter-spacing:3px;color:#f3c9cb}
  .card-back .brand{position:absolute;right:36px;top:34px;flex-direction:column;align-items:flex-end;gap:6px;font-size:18px}
  .card-back .brand .dot{width:22px;height:22px;margin-right:26px}
  .card-back .owner{position:absolute;right:36px;top:96px;font-family:"Oswald",sans-serif;font-size:7.5px;letter-spacing:.3px;color:var(--slate-text)}
  .card-back .owner b{font-weight:500;color:#c9d0d5}
  .card-back .contact{position:absolute;left:8px;bottom:8px;font-family:"Oswald",sans-serif;font-weight:300;font-size:7px;color:var(--slate-text);letter-spacing:.2px}
  .card-back .contact b{font-weight:500;color:#fff}
</style>
</head>
<body>
<div class="canvas">
  <div class="crop" style="left:0;top:51px;width:30px;height:1px"></div>
  <div class="crop" style="left:48px;top:0;width:1px;height:30px"></div>
  <div class="crop" style="right:0;top:51px;width:30px;height:1px"></div>
  <div class="crop" style="left:916px;top:0;width:1px;height:30px"></div>
  <div class="crop" style="left:0;top:1149px;width:30px;height:1px"></div>
  <div class="crop" style="left:48px;top:1170px;width:1px;height:30px"></div>
  <div class="crop" style="right:0;top:1149px;width:30px;height:1px"></div>
  <div class="crop" style="left:916px;top:1170px;width:1px;height:30px"></div>

  <div class="sheet-edge"></div>
  <div class="backdrop-area" role="img" aria-label="Faint oversized brand mark decoration in pale green"></div>

  <header class="header">
    <div class="brand"><span class="dot"></span>Plovenix</div>
    <div class="rule"></div>
  </header>
  <div class="contact-bar">
    <span><b>Tel:</b> 00 555 01234</span><span class="sep">|</span>
    <span><b>Fax:</b> 00 555 01234</span><span class="sep">|</span>
    <span><b>E-mail</b> : hello@plovenix.com</span><span class="sep">|</span>
    <span><b>Website</b> : www.plovenix.com</span><span class="sep">|</span>
    <span><b>Location</b> : Cedar Vale, USA.</span>
  </div>

  <div class="hero">
    <div class="dot"></div>
    <div class="name">Plovenix</div>
  </div>

  <section class="card card-front">
    <div class="brand"><span class="dot"></span>Plovenix</div>
    <div class="rule"></div>
  </section>

  <section class="card card-back">
    <div class="brand"><span class="dot"></span>Plovenix</div>
    <div class="owner"><b>Name of the Owner</b> | Designation</div>
    <div class="contact"><b>Tel:</b> 00 555 01234, <b>Fax:</b> 00 555 01234, <b>E-mail</b> : hello@plovenix.com</div>
    <div class="strip"><span>www.plovenix.com</span></div>
  </section>
</div>
</body>
</html>
```